Brightmoor Law Letterhead for Law firm must be modern and use the logo I uploaded.

Hello I want a clean modern professional letterhead for my law firm Brightmoor Law. A logo has already been created and all files have been uploaded. The information for the firm can be given through message. Please use the logo that has already been created. Please also use the color scheme of that logo. (blue and white).

Target Market(s)

General Public

Industry/Entity Type

Law Firm

Colors

Designer to choose colors to be used in the design.

Requirements
Must have
• This must be a modern professional letterhead
Nice to have
• My logo that is included in file form
Should not have
• Should not have logo that is not the one I uploaded.

```html
<!DOCTYPE html>
<html lang="en">
<head>
<meta charset="utf-8">
<title>Brightmoor Law Letterhead</title>
<link rel="stylesheet" href="https://fonts.googleapis.com/css2?family=Montserrat:wght@400;600&family=Questrial&family=Lato:wght@400&family=Open+Sans:wght@600&display=swap">
<style>
  :root {
    --navy: #2b2d5c;
    --ink-grey: #8a8a8c;
    --body-grey: #8f8f91;
    --name-grey: #9d9ea0;
    --address-grey: #5b5b5d;
    --rule: #8a8a8a;
    --paper: #ffffff;
    --backdrop: #e4e4e6;
    --sign-tone: #ececee;
  }
  * { margin: 0; padding: 0; box-sizing: border-box; }
  html, body { width: 1051px; height: 1200px; overflow: hidden; background: var(--backdrop); }
  .letterhead {
    position: absolute; left: 109px; top: 16px;
    width: 832px; height: 1167px;
    background: var(--paper);
    box-shadow: 0 2px 10px rgba(0,0,0,0.12);
  }
  .brand-name {
    position: absolute; left: 35px; top: 99px;
    font-family: "Montserrat", sans-serif; font-weight: 600;
    font-size: 13px; letter-spacing: 7px; color: var(--navy);
  }
  .firm-address {
    position: absolute; right: 63px; top: 53px;
    text-align: right;
    font-family: "Lato", sans-serif; font-size: 14.5px; line-height: 19px;
    color: var(--address-grey);
  }
  .pin-icon { position: absolute; right: 38px; top: 55px; width: 20px; height: 20px; }
  .recipient { position: absolute; left: 40px; top: 286px; font-family: "Montserrat", sans-serif; color: var(--ink-grey); }
  .recipient-name { font-weight: 600; font-size: 26px; color: var(--name-grey); letter-spacing: 0.5px; margin-bottom: 8px; }
  .recipient-line { font-size: 14.5px; line-height: 19px; margin-bottom: 8px; letter-spacing: 0.3px; }
  .letter-date {
    position: absolute; right: 36px; top: 392px;
    font-family: "Open Sans", sans-serif; font-weight: 600; font-size: 16px;
    color: var(--ink-grey);
  }
  .letter-body {
    position: absolute; left: 36px; right: 36px; top: 448px;
    font-family: "Questrial", sans-serif; font-size: 15px; line-height: 19.2px;
    color: var(--body-grey); text-align: justify; hyphens: auto;
  }
  .letter-body p { margin-bottom: 19px; }
  .letter-body p.tight { margin-bottom: 0; }
  .letter-body p.after-tight { margin-top: 0; }
  .letter-body p.spaced { margin-top: 0; padding-top: 22px; }
  .signatory-title {
    position: absolute; left: 553px; top: 841px;
    font-family: "Questrial", sans-serif; font-size: 20px; color: var(--ink-grey);
  }
  .signature-area {
    position: absolute; left: 569px; top: 882px; width: 155px; height: 97px;
    background: var(--sign-tone);
  }
  .contact-list {
    position: absolute; left: 36px; top: 1055px; list-style: none;
    font-family: "Lato", sans-serif; font-size: 14.5px; color: var(--address-grey);
  }
  .contact-list li { display: flex; align-items: center; height: 17px; margin-bottom: 11px; }
  .contact-list svg { width: 17px; height: 17px; margin-right: 4px; flex: none; }
  .footer-rule {
    position: absolute; left: 238px; right: 0; top: 1121px;
    border-top: 1px solid var(--rule);
  }
</style>
</head>
<body>
  <main class="letterhead">
    <div class="brand-name">BRIGHTMOOR LAW</div>

    <address class="firm-address" style="font-style:normal">2217 Harlow Avenue<br>Washington, DC 20031</address>
    <svg class="pin-icon" viewBox="0 0 20 20" aria-hidden="true">
      <rect width="20" height="20" rx="2" fill="var(--navy)"/>
      <path d="M10 3.5a4.3 4.3 0 0 0-4.3 4.3c0 3.2 4.3 8.2 4.3 8.2s4.3-5 4.3-8.2A4.3 4.3 0 0 0 10 3.5z" fill="#fff"/>
      <circle cx="10" cy="7.8" r="1.7" fill="var(--navy)"/>
    </svg>

    <section class="recipient">
      <h1 class="recipient-name">DANA WHITFIELD</h1>
      <p class="recipient-line">0214-555-0187</p>
      <p class="recipient-line">dana@brightmoorlaw.com</p>
      <p class="recipient-line">880 Cedar Ridge Ln. Suite<br>410 Dallas, TX 75201</p>
    </section>

    <div class="letter-date">12 December, 2023</div>

    <section class="letter-body">
      <p>Lorem ipsum dolor sit amet, consectetuer adipiscing elit, sed diam nonummy nibh euismod tincidunt ut laoreet dolore magna aliquam erat volutpat. Ut wisi enim ad minim veniam, quis nostrud exerci tation ullamcorper suscipit lobortis nisl ut aliquip ex ea commodo consequat. Duis autem vel eum iriure dolor in hendrerit in vulputate velit esse molestie consequat, vel illum dolore eu feugiat nulla facilisis at vero eros et accumsan et iusto odio dignissim qui blandit praesent luptatum zzril delenit augue duis dolore te feugait nulla facilisi.</p>
      <p class="tight">Lorem ipsum dolor sit amet, cons ectetuer adipiscing elit, sed diam nonummy nibh euismod tincidunt ut laoreet dolore magna aliquam erat volutpat. Ut wisi enim ad minim veniam, quis nostrud exerci tation ullamcorper suscipit lobortis nisl ut aliquip ex ea commodo consequat.</p>
      <p class="after-tight">Lorem ipsum dolor sit amet, consectetuer adipiscing elit, sed diam nonummy nibh euismod tincidunt ut laoreet dolore magna aliquam erat</p>
      <p class="spaced">Lorem ipsum dolor sit amet, cons ectetuer adipiscing elit, sed diam nonummy nibh euismod tincidunt ut laoreet dolore magna aliquam erat volutpat. Ut wisi enim ad minim veniam, quis nostrud exerci tation ullamcorper suscipit lobortis nisl ut aliquip ex ea commodo consequat. Lorem ipsum dolor sit zamet, consectetuer adipiscing elit, sed diam nonummy nibh euismod tincidunt.</p>
    </section>

    <div class="signatory-title">Managing Director</div>
    <div class="signature-area" role="img" aria-label="Handwritten signature of the managing director"></div>

    <ul class="contact-list">
      <li>
        <svg viewBox="0 0 17 17" aria-hidden="true"><rect width="17" height="17" rx="2" fill="var(--navy)"/><path d="M5 3.5l2 2.3-1.1 1.4a7 7 0 0 0 3.9 3.9l1.4-1.1 2.3 2-1.2 1.6C8.6 13.4 3.6 8.4 3.4 4.7z" fill="#fff"/></svg>
        +00 202 555 01
      </li>
      <li>
        <svg viewBox="0 0 17 17" aria-hidden="true"><rect width="17" height="17" rx="2" fill="var(--navy)"/><rect x="3" y="5" width="11" height="7.5" fill="none" stroke="#fff" stroke-width="1.1"/><path d="M3 5l5.5 4.3L14 5M3 12.5l4.2-3.6M14 12.5l-4.2-3.6" fill="none" stroke="#fff" stroke-width="1.1"/></svg>
        office@brightmoorlaw.com
      </li>
      <li>
        <svg viewBox="0 0 17 17" aria-hidden="true"><rect width="17" height="17" rx="2" fill="var(--navy)"/><path d="M5.5 3.5v9.5l2.3-2.2 1.6 3.4 1.5-.7-1.6-3.3h3.2z" fill="#fff"/></svg>
        www.brightmoorlaw.com
      </li>
    </ul>
    <div class="footer-rule"></div>
  </main>
</body>
</html>
```